Brovantix Friendlane Page*

Looking for someone to design and set up our Friendlane page!

We sell luxury men's accessories. Website url is brovantix.com

Target Market(s)

Men and women, medium age 42, has disposable income.

Industry/Entity Type

Retail

Font styles to use
Sans Serif

Colors

Designer to choose colors to be used in the design.

Requirements
Must have
• Language or images or theme tied to "Gifts for Men".
• We are optimizing our site to target keywords and theme "gifts for men" and "luxury gifts for men".

```html
<!DOCTYPE html>
<html lang="en">
<head>
<meta charset="utf-8">
<title>Brovantix – Page Cover</title>
<link href="https://fonts.googleapis.com/css2?family=Montserrat:wght@400;600;700;800&family=Roboto:wght@400;500;700&display=swap" rel="stylesheet">
<style>
:root{
  --ink:#111;
  --black:#050505;
  --white:#fff;
  --paper:#f3f3f3;
  --page-bg:#e9ebee;
  --bar:#4267b2;
  --bar-dark:#29487d;
  --line:#dddfe2;
  --text:#1d2129;
  --muted:#606770;
  --link:#385898;
  --green:#42b72a;
  --accent:#e8263a;
}
*{box-sizing:border-box;margin:0;padding:0}
html,body{width:1200px;height:1200px;overflow:hidden;background:var(--white)}
body{position:relative;font-family:Roboto,Arial,sans-serif;color:var(--text)}

.sheet-label{position:absolute;left:46px;top:140px;width:30px;height:160px;display:flex;align-items:center;justify-content:center}
.sheet-label span{transform:rotate(-90deg);white-space:nowrap;font-family:Montserrat,sans-serif;font-size:32px;font-weight:400;color:var(--ink);letter-spacing:1px}

/* Cover artwork, sized in em */
.cover{position:absolute;width:101.6em;height:37.6em;overflow:hidden;background:var(--paper);font-family:Montserrat,sans-serif}
.cover--hero{left:112px;top:20px;font-size:10px;box-shadow:0 2px 6px rgba(0,0,0,.35)}
.cover--page{left:237px;top:44px;font-size:8.46px;height:38.4em}
.cover__dark{position:absolute;left:0;top:0;width:56em;height:100%;background:var(--black)}
.cover__portrait{position:absolute;left:33em;top:0;width:23em;height:100%;background:radial-gradient(ellipse at 55% 45%,#5a4a44 0%,#2b2220 45%,#0b0a0a 80%)}
.cover__ribbon{position:absolute;left:53.5em;top:0;width:4.5em;height:100%;background:linear-gradient(90deg,#6d6d6d,#e8e8e8 40%,#9a9a9a 70%,#f1f1f1);transform:skewX(3deg)}
.cover__couple{position:absolute;left:57.5em;top:0;right:0;height:100%;background:radial-gradient(ellipse at 45% 55%,#b9b9b9 0%,#dcdcdc 45%,#f4f4f4 80%)}
.cover__copy{position:absolute;left:0;top:0;width:43em;height:100%;color:var(--white);text-align:center}
.cover__line{position:absolute;left:0;width:100%;line-height:1;white-space:nowrap}
.cover__line span{display:inline-block}
.cover__line--logo{top:2.4em}
.cover__line--logo span{font-size:5.4em;font-weight:600}
.cover__line--name{top:10.4em}
.cover__line--name span{font-size:3.3em;font-weight:400;letter-spacing:.16em}
.cover__line--kicker{top:18.3em}
.cover__line--kicker span{font-size:2.3em;font-weight:700}
.cover__line--headline{top:21.2em}
.cover__line--headline-2{top:25.8em}
.cover__line--headline span,.cover__line--headline-2 span{font-size:3.9em;font-weight:800}
.cover__line--url{top:32.4em;display:flex;justify-content:center;align-items:center;gap:.6em}
.cover__line--url span{font-size:1.9em;font-weight:600;letter-spacing:.18em}
.cover__line--url svg{width:2.2em;height:2.2em}
.cover__rule{position:absolute;left:6.8em;width:29.4em;height:.2em;background:linear-gradient(90deg,transparent,#8a8a8a 30%,#8a8a8a 70%,transparent)}
.cover__rule--top{top:16.8em}
.cover__rule--bottom{top:30.8em}

/* Page mockup */
.page{position:absolute;left:0;top:418px;width:1200px;height:782px;background:var(--page-bg)}
.topbar{position:absolute;left:0;top:0;width:1200px;height:44px;background:var(--bar);border-bottom:1px solid var(--bar-dark)}
.topbar__brand{position:absolute;left:36px;top:10px;width:26px;height:26px;border-radius:3px;background:var(--white)}
.topbar__search{position:absolute;left:70px;top:9px;width:466px;height:25px;background:var(--white);border-radius:2px}
.topbar__search svg{position:absolute;right:12px;top:5px}
.topbar__nav{position:absolute;left:770px;top:0;height:44px;display:flex;align-items:center;color:var(--white);font-size:13px;font-weight:700}
.topbar__nav a{padding:0 12px;border-left:1px solid rgba(255,255,255,.25);color:inherit;text-decoration:none}
.topbar__icons{position:absolute;left:905px;top:11px;display:flex;gap:22px;align-items:center}

.avatar{position:absolute;left:39px;top:58px;width:186px;height:186px;border-radius:50%;background:var(--black);border:5px solid var(--white);display:flex;align-items:center;justify-content:center;color:var(--white);font-family:Montserrat,sans-serif;font-weight:600;font-size:28px}

.sidenav{position:absolute;left:35px;top:384px;width:187px;list-style:none;font-size:14px;color:#4b4f56}
.sidenav li{height:32.5px;line-height:30px;padding-left:8px}
.sidenav li.is-active{background:#f5f6f7;border:1px solid var(--line);font-weight:700;color:var(--text)}
.btn-create{position:absolute;left:40px;top:624px;width:97px;height:23px;background:var(--green);color:var(--white);font-size:12px;font-weight:700;border-radius:2px;text-align:center;line-height:23px}

.panel{position:absolute;background:var(--white);border:1px solid var(--line);border-radius:3px}
.actions{left:237px;top:372px;width:860px;height:53px}
.action-group{position:absolute;left:13px;top:11px;height:29px;display:flex;border:1px solid #ccd0d5;border-radius:2px;font-size:13px;font-weight:700;color:#4b4f56}
.action-group span{display:flex;align-items:center;gap:5px;padding:0 11px;border-right:1px solid #ccd0d5}
.action-group span:last-child{border:0}
.btn{position:absolute;top:11px;height:29px;font-size:15px;display:flex;align-items:center;justify-content:center;gap:6px;border-radius:2px}
.btn--email{left:544px;width:148px;background:var(--bar);color:var(--white)}
.btn--msg{left:705px;width:141px;background:#f5f6f7;border:1px solid #ccd0d5;color:#4b4f56}

.composer{left:237px;top:439px;width:524px;height:163px}
.composer__title{position:absolute;left:32px;top:12px;font-size:13px;font-weight:500;color:#4b4f56}
.composer__rule{position:absolute;left:13px;right:13px;top:36px;height:1px;background:var(--line)}
.composer__avatar{position:absolute;left:13px;top:48px;width:44px;height:44px;border-radius:50%;background:var(--black);color:var(--white);font-family:Montserrat,sans-serif;font-size:7px;font-weight:600;display:flex;align-items:center;justify-content:center}
.composer__input{position:absolute;left:68px;top:62px;font-size:15px;color:#90949c}
.composer__tools{position:absolute;left:13px;top:120px;display:flex;gap:9px}
.chip{height:33px;padding:0 14px;background:#f5f6f7;border-radius:17px;display:flex;align-items:center;gap:7px;font-size:13px;color:#4b4f56;font-weight:500}

.photos{left:237px;top:614px;width:524px;height:180px}
.panel__head{position:absolute;left:13px;top:12px;font-size:15px;font-weight:700}
.photos .panel__rule{position:absolute;left:0;right:0;top:42px;height:1px;background:var(--line)}

.rating{left:773px;top:439px;width:323px;height:60px;display:flex;align-items:center;gap:12px;padding-left:15px;font-size:13px}
.rating i{width:30px;height:30px;border-radius:50%;background:#90949c;display:block}
.community{left:773px;top:512px;width:323px;height:72px}
.about{left:773px;top:596px;width:323px;height:200px}
.see-all{position:absolute;right:13px;top:14px;font-size:13px;color:var(--muted)}
.invite{position:absolute;left:13px;top:46px;font-size:13px;display:flex;gap:10px;align-items:center}
.invite b{color:var(--link);font-weight:500}
.about__icons{position:absolute;left:13px;top:44px;display:flex;flex-direction:column;gap:11px}
</style>
</head>
<body>

<div class="sheet-label"><span>COVER FL</span></div>

<section class="cover cover--hero">
  <div class="cover__dark"></div>
  <div class="cover__portrait" role="img" aria-label="Photo of a well-dressed man in a waistcoat seated in a carved leather armchair"></div>
  <div class="cover__couple" role="img" aria-label="Black and white photo of a woman covering a smiling man's eyes while handing him a red-ribboned gift"></div>
  <div class="cover__ribbon" role="img" aria-label="Silver satin ribbon with bow dividing the cover"></div>
  <div class="cover__copy">
    <div class="cover__line cover__line--logo"><span>Brovantix</span></div>
    <div class="cover__line cover__line--name"><span>BROVANTIX</span></div>
    <div class="cover__rule cover__rule--top"></div>
    <div class="cover__line cover__line--kicker"><span>PURVEYORS OF FINE &amp;</span></div>
    <div class="cover__line cover__line--headline"><span>LUXURIOUS GIFTS</span></div>
    <div class="cover__line cover__line--headline-2"><span>FOR MEN</span></div>
    <div class="cover__rule cover__rule--bottom"></div>
    <div class="cover__line cover__line--url"><svg viewBox="0 0 24 24" fill="none" stroke="#fff" stroke-width="2"><circle cx="12" cy="12" r="10"/><path d="M2 12h20M12 2c3 3 3 17 0 20M12 2c-3 3-3 17 0 20"/></svg><span>www.brovantix.com</span></div>
  </div>
</section>

<section class="page">
  <header class="topbar">
    <div class="topbar__brand" aria-label="Friendlane"></div>
    <div class="topbar__search"><svg width="16" height="16" viewBox="0 0 16 16" fill="none" stroke="#4b4f56" stroke-width="2"><circle cx="6.5" cy="6.5" r="5"/><path d="M10 10l5 5"/></svg></div>
    <nav class="topbar__nav"><a>Home</a><a>Create</a></nav>
    <div class="topbar__icons">
      <svg width="22" height="20" viewBox="0 0 22 20" fill="#1d2a5b"><circle cx="7" cy="6" r="4"/><circle cx="15" cy="6" r="3.5"/><path d="M0 19c0-5 3-7 7-7s7 2 7 7zM14 12c4 0 8 2 8 7h-7c0-3-1-5-1-7z"/></svg>
      <svg width="22" height="22" viewBox="0 0 22 22" fill="#1d2a5b"><path d="M11 1C5 1 1 5 1 10c0 3 1.5 5 3.5 6.5V21l4-2.2c.8.2 1.6.2 2.5.2 6 0 10-4 10-9S17 1 11 1z"/></svg>
      <svg width="20" height="22" viewBox="0 0 20 22" fill="#1d2a5b"><path d="M10 1c4 0 6 3 6 7v5l3 4H1l3-4V8c0-4 2-7 6-7zM7 19h6a3 3 0 0 1-6 0z"/></svg>
      <svg width="22" height="22" viewBox="0 0 22 22"><circle cx="11" cy="11" r="10" fill="#1d2a5b"/><text x="11" y="16" text-anchor="middle" font-size="14" font-weight="700" fill="#4267b2" font-family="Roboto,sans-serif">?</text></svg>
      <svg width="14" height="10" viewBox="0 0 14 10" fill="#1d2a5b"><path d="M1 2h12L7 9z"/></svg>
    </div>
  </header>

  <section class="cover cover--page">
    <div class="cover__dark"></div>
    <div class="cover__portrait" role="img" aria-label="Photo of a well-dressed man in a waistcoat seated in a carved leather armchair"></div>
    <div class="cover__couple" role="img" aria-label="Black and white photo of a woman covering a smiling man's eyes while handing him a red-ribboned gift"></div>
    <div class="cover__ribbon" role="img" aria-label="Silver satin ribbon with bow dividing the cover"></div>
    <div class="cover__copy">
      <div class="cover__line cover__line--logo"><span>Brovantix</span></div>
      <div class="cover__line cover__line--name"><span>BROVANTIX</span></div>
      <div class="cover__rule cover__rule--top"></div>
      <div class="cover__line cover__line--kicker"><span>PURVEYORS OF FINE &amp;</span></div>
      <div class="cover__line cover__line--headline"><span>LUXURIOUS GIFTS</span></div>
      <div class="cover__line cover__line--headline-2"><span>FOR MEN</span></div>
      <div class="cover__rule cover__rule--bottom"></div>
      <div class="cover__line cover__line--url"><svg viewBox="0 0 24 24" fill="none" stroke="#fff" stroke-width="2"><circle cx="12" cy="12" r="10"/><path d="M2 12h20M12 2c3 3 3 17 0 20M12 2c-3 3-3 17 0 20"/></svg><span>www.brovantix.com</span></div>
    </div>
  </section>

  <div class="avatar">Brovantix</div>

  <ul class="sidenav">
    <li class="is-active">Home</li><li>Services</li><li>Reviews</li><li>Photos</li><li>Posts</li><li>About</li><li>Community</li>
  </ul>
  <div class="btn-create">Create a Page</div>

  <div class="panel actions">
    <div class="action-group">
      <span><svg width="12" height="12" viewBox="0 0 12 12" fill="#4b4f56"><path d="M0 5h3v7H0zM4 5l3-5c1 0 2 1 1.5 3H12v3l-2 6H4z"/></svg>Like</span>
      <span><svg width="13" height="13" viewBox="0 0 13 13" fill="none" stroke="#4b4f56" stroke-width="1.6"><path d="M1 1a11 11 0 0 1 11 11M1 5a7 7 0 0 1 7 7"/><circle cx="2" cy="11" r="1.3" fill="#4b4f56"/></svg>Follow</span>
      <span><svg width="14" height="12" viewBox="0 0 14 12" fill="#4b4f56"><path d="M8 0l6 5-6 5V7C4 7 2 8 0 12c0-5 3-8 8-8z"/></svg>Share</span>
      <span>•••</span>
    </div>
    <div class="btn btn--email">Send Email</div>
    <div class="btn btn--msg"><svg width="16" height="16" viewBox="0 0 22 22" fill="#4b4f56"><path d="M11 1C5 1 1 5 1 10c0 3 1.5 5 3.5 6.5V21l4-2.2c.8.2 1.6.2 2.5.2 6 0 10-4 10-9S17 1 11 1z"/></svg>Send Message</div>
  </div>

  <div class="panel composer">
    <div class="composer__title">Create Post</div>
    <div class="composer__rule"></div>
    <div class="composer__avatar">Brovantix</div>
    <div class="composer__input">Write a post...</div>
    <div class="composer__tools">
      <div class="chip"><svg width="18" height="16" viewBox="0 0 18 16"><rect x="1" y="1" width="16" height="14" rx="2" fill="#58c472"/><path d="M2 14l5-6 4 4 2-2 4 4z" fill="#fff"/></svg>Photo/Video</div>
      <div class="chip"><svg width="18" height="16" viewBox="0 0 18 16" fill="#4a7fd6"><circle cx="7" cy="5" r="4"/><path d="M0 16c0-5 3-7 7-7s7 2 7 7z"/></svg>Tag Friends</div>
      <div class="chip"><svg width="14" height="18" viewBox="0 0 14 18"><path d="M7 0a7 7 0 0 1 7 7c0 5-7 11-7 11S0 12 0 7a7 7 0 0 1 7-7z" fill="var(--accent)"/><circle cx="7" cy="7" r="2.5" fill="#fff"/></svg>Check in</div>
      <div class="chip">•••</div>
    </div>
  </div>

  <div class="panel photos"><div class="panel__head">Photos</div><div class="panel__rule"></div></div>

  <div class="panel rating"><i></i>No Rating Yet</div>
  <div class="panel community"><div class="panel__head">Community</div><div class="see-all">See All</div>
    <div class="invite"><svg width="16" height="14" viewBox="0 0 16 14" fill="#90949c"><circle cx="5" cy="4" r="3"/><circle cx="11" cy="4" r="2.5"/><path d="M0 14c0-4 2-5 5-5s5 1 5 5zM11 9c3 0 5 1 5 5h-5z"/></svg><span><b>Invite your friends</b> to like this Page</span></div>
  </div>
  <div class="panel about"><div class="panel__head">About</div><div class="see-all">See All</div>
    <div class="about__icons">
      <svg width="18" height="18" viewBox="0 0 18 18" fill="none" stroke="#606770" stroke-width="1.3"><path d="M4 1l3 4-2 2c1 3 3 5 6 6l2-2 4 3-2 3C8 17 1 10 1 3z"/></svg>
      <svg width="18" height="18" viewBox="0 0 22 22" fill="none" stroke="#606770" stroke-width="1.5"><path d="M11 1C5 1 1 5 1 10c0 3 1.5 5 3.5 6.5V21l4-2.2c.8.2 1.6.2 2.5.2 6 0 10-4 10-9S17 1 11 1z"/></svg>
      <svg width="18" height="18" viewBox="0 0 24 24" fill="none" stroke="#606770" stroke-width="1.6"><circle cx="12" cy="12" r="10"/><path d="M2 12h20M12 2c3 3 3 17 0 20M12 2c-3 3-3 17 0 20"/></svg>
      <svg width="18" height="16" viewBox="0 0 18 16" fill="none" stroke="#606770" stroke-width="1.3"><rect x="1" y="1" width="16" height="14"/><path d="M1 5h16"/></svg>
      <svg width="18" height="18" viewBox="0 0 18 18" fill="none" stroke="#606770" stroke-width="1.3"><path d="M13 1l4 4L6 16H2v-4z"/></svg>
    </div>
  </div>
</section>

</body>
</html>
```